Hintergrund Design für Flyer und Plakate für Spanischschule
Kreativ, Kompetent, Profesionell und die Zusammenarbeit war sehr angenehm. Sehr gerne wieder.
Zielgruppe
Erwachsene, Kinder Eltern, Familie,
Schulen und Einrichtungen, Firmen
Aufgabenstellung
Das Layout soll multifunktional sein, das heist in seinen Grundzügen oder leicht abgewandelt soll es für Postkarten, Flyer (DIN A 4 - 3 fach geknickt) und evtl. Plakate (als Hintergrund) Verwendung finden.
Und es soll für verschiedene Projekte / Veranstaltungen wiederverwendet werden.

```html
<!DOCTYPE html>
<html lang="de">
<head>
<meta charset="utf-8">
<title>Casa Idioma – Hintergrund</title>
<link rel="stylesheet" href="https://fonts.googleapis.com/css2?family=Amatic+SC:wght@700&display=swap">
<style>
  :root {
    --orange-deep: #e2611c;
    --orange-mid: #ec7a26;
    --orange-light: #f39a3a;
    --orange-warm: #d9501a;
    --paper: #f6f6f6;
    --outline: #ffffff;
    --brand-ink: #e27b14;
  }
  html, body {
    margin: 0;
    padding: 0;
    overflow: hidden;
    background: #ffffff;
  }
  .poster {
    position: relative;
    width: 848px;
    height: 1200px;
    overflow: hidden;
    background:
      repeating-linear-gradient(180deg,
        var(--orange-mid) 0 14px,
        var(--orange-deep) 14px 22px,
        var(--orange-light) 22px 30px,
        var(--orange-warm) 30px 41px,
        var(--orange-mid) 41px 58px,
        var(--orange-light) 58px 63px);
  }
  .poster__shapes {
    position: absolute;
    inset: 0;
    width: 848px;
    height: 1200px;
  }
  .brand {
    position: absolute;
    left: 550px;
    top: 170px;
    width: 290px;
    display: flex;
    align-items: center;
    justify-content: center;
    gap: 10px;
  }
  .brand__dot {
    width: 16px;
    height: 16px;
    border-radius: 50%;
    background: var(--brand-ink);
    flex: none;
  }
  .brand__name {
    font-family: "Amatic SC", "Comic Sans MS", cursive;
    font-weight: 700;
    font-size: 50px;
    line-height: 1;
    color: var(--brand-ink);
    letter-spacing: 1px;
    white-space: nowrap;
  }
</style>
</head>
<body>
  <main class="poster">
    <svg class="poster__shapes" viewBox="0 0 590 835" preserveAspectRatio="none" aria-hidden="true">
      <!-- outlined speech bubbles along the top edge -->
      <g fill="none" stroke="var(--outline)" stroke-width="3" stroke-linecap="round">
        <path d="M285,0 C282,20 295,40 318,42 L325,58 L330,40 C345,34 350,14 345,0"/>
        <path d="M545,0 C545,15 555,25 570,25 L578,40 L582,22 C590,18 592,10 590,0"/>
      </g>
      <!-- main open writing area, curving around the logo bubble -->
      <path class="poster__field" fill="var(--paper)"
        d="M0,78 C60,70 150,80 240,72 C290,68 330,74 355,72
           C345,110 350,160 362,190 C375,215 400,230 428,236
           C480,244 545,236 570,224 C580,218 586,210 590,205
           L590,590 C565,640 535,700 470,720
           C400,742 305,738 258,768 C242,792 246,820 246,835
           L110,835 C104,760 92,704 48,682 C25,672 8,676 0,672 Z"/>
      <!-- logo speech bubble, tail reaching into the writing area -->
      <path class="poster__brand-bubble" fill="var(--paper)"
        d="M380,95 C378,55 400,34 440,28 C490,22 545,22 568,36
           C585,48 587,90 585,130 C583,170 575,200 550,212
           C520,222 480,222 458,220 L446,256 L434,216
           C400,210 378,190 374,160 C370,130 382,115 380,95 Z"/>
    </svg>
    <div class="brand">
      <span class="brand__dot"></span>
      <span class="brand__name">Casa Idioma</span>
    </div>
  </main>
</body>
</html>
```